residential roofing company needs a Truck wrap design.

We need a Van wrap design. We are a local residential roofing contractor.That specialize in Roofing Eavestrough and siding we need a design that will stand out and look professional.We really want roofing to stand out as that's our main focus. We like a clean a simple and modern design. Our website is www.larkfieldexteriors.ca The van we are wrapping is a 2019 Halvorsen-Kraft Tolvane 2500 Cargo 170 WB High Roof. We want to incorporate our phone number 844 612 DECK

```html
<!DOCTYPE html>
<html lang="en">
<head>
<meta charset="utf-8">
<title>Larkfield Exteriors – Van Wrap</title>
<link rel="stylesheet" href="https://fonts.googleapis.com/css2?family=Montserrat:wght@600;800&family=Saira:wght@700&display=swap">
<style>
  :root {
    --canvas: #e9ecef;
    --wrap-white: #ffffff;
    --band-grey: #5e5e5e;
    --stripe-grey: #6b6b6b;
    --brand-yellow: #e8a823;
    --web-grey: #555555;
    --photo-sky: #7fa6c9;
    --photo-house: #c9d3dc;
    --photo-roof: #5a5d63;
    --photo-brown: #8a6a52;
    --edge: #2c2c2c;
  }
  html, body {
    margin: 0;
    width: 1200px;
    height: 1051px;
    overflow: hidden;
    background: var(--canvas);
  }
  .wrap-sheet { display: block; width: 1200px; height: 1051px; }
  .panel-body { fill: var(--wrap-white); stroke: #cfd3d7; stroke-width: 2; }
  .brand-band { fill: var(--band-grey); }
  .contact-stripe { fill: var(--stripe-grey); }
  .brand-square { fill: var(--brand-yellow); }
  .brand-name {
    font-family: "Montserrat", sans-serif;
    font-weight: 800;
    fill: var(--wrap-white);
  }
  .tagline {
    font-family: "Montserrat", sans-serif;
    font-weight: 600;
    fill: var(--wrap-white);
  }
  .phone {
    font-family: "Saira", sans-serif;
    font-weight: 700;
    fill: var(--brand-yellow);
  }
  .website {
    font-family: "Saira", sans-serif;
    font-weight: 700;
    fill: var(--web-grey);
  }
  .photo-frame { stroke: var(--edge); stroke-width: 4; }
</style>
</head>
<body>
<svg class="wrap-sheet" viewBox="0 0 1200 1051" xmlns="http://www.w3.org/2000/svg">
  <defs>
    <linearGradient id="house-tones" x1="0" y1="0" x2="0" y2="1">
      <stop offset="0" stop-color="#7fa6c9"/>
      <stop offset="0.55" stop-color="#c9d3dc"/>
      <stop offset="1" stop-color="#5f8a4f"/>
    </linearGradient>
    <linearGradient id="roof-tones" x1="0" y1="0" x2="1" y2="1">
      <stop offset="0" stop-color="#5a5d63"/>
      <stop offset="1" stop-color="#b9b3aa"/>
    </linearGradient>
    <linearGradient id="brown-tones" x1="0" y1="0" x2="0" y2="1">
      <stop offset="0" stop-color="#8a6a52"/>
      <stop offset="1" stop-color="#d9d2c6"/>
    </linearGradient>
  </defs>

  <g class="side side-driver" transform="translate(40 40)">
    <rect class="panel-body" x="0" y="0" width="1120" height="450" rx="40"/>
    <polygon class="brand-band" points="600,55 1090,55 1090,275 540,275 610,205"/>
    <rect class="brand-square" x="380" y="60" width="210" height="210"/>
    <text class="brand-name" x="638" y="150" font-size="76" textLength="440" lengthAdjust="spacingAndGlyphs">LARKFIELD</text>
    <text class="brand-name" x="638" y="203" font-size="46" textLength="440" lengthAdjust="spacingAndGlyphs">EXTERIORS.ca</text>
    <text class="tagline" x="640" y="240" font-size="21" textLength="436" lengthAdjust="spacing">ROOFING &amp; EXTERIORS</text>
    <rect class="contact-stripe" x="380" y="303" width="710" height="35"/>
    <text class="phone" x="408" y="334" font-size="30">Call Us: 844 612 DECK</text>
    <text class="website" x="392" y="375" font-size="24">www.larkfieldexteriors.ca</text>
    <polygon class="photo-frame" role="img" aria-label="Photo of a white two-storey house with a new roof" fill="url(#house-tones)" points="230,150 310,196 310,288 230,334 150,288 150,196"/>
    <polygon class="photo-frame" role="img" aria-label="Photo of a dark shingle roof close-up" fill="url(#roof-tones)" points="340,218 396,250 396,314 340,346 284,314 284,250"/>
    <polygon class="photo-frame" role="img" aria-label="Photo of a house with a brown roof and porch" fill="url(#brown-tones)" points="320,330 376,362 376,430 264,430 264,362"/>
  </g>

  <g class="side side-passenger" transform="translate(40 560)">
    <rect class="panel-body" x="0" y="0" width="1120" height="450" rx="40"/>
    <polygon class="brand-band" points="30,55 640,55 590,100 590,275 30,275"/>
    <rect class="brand-square" x="600" y="60" width="210" height="210"/>
    <text class="brand-name" x="75" y="150" font-size="76" textLength="440" lengthAdjust="spacingAndGlyphs">LARKFIELD</text>
    <text class="brand-name" x="75" y="203" font-size="46" textLength="440" lengthAdjust="spacingAndGlyphs">EXTERIORS.ca</text>
    <text class="tagline" x="77" y="240" font-size="21" textLength="436" lengthAdjust="spacing">ROOFING &amp; EXTERIORS</text>
    <rect class="contact-stripe" x="30" y="303" width="740" height="35"/>
    <text class="phone" x="390" y="334" font-size="30">Call Us: 844 612 DECK</text>
    <text class="website" x="372" y="375" font-size="24">www.larkfieldexteriors.ca</text>
    <polygon class="photo-frame" role="img" aria-label="Photo of a dark shingle roof close-up" fill="url(#roof-tones)" points="780,230 836,262 836,326 780,358 724,326 724,262"/>
    <polygon class="photo-frame" role="img" aria-label="Photo of a white two-storey house with a new roof" fill="url(#house-tones)" points="910,150 990,196 990,288 910,334 830,288 830,196"/>
    <polygon class="photo-frame" role="img" aria-label="Photo of a house with a brown roof and porch" fill="url(#brown-tones)" points="830,338 886,370 886,430 774,430 774,370"/>
  </g>
</svg>
</body>
</html>
```